Business card design needed

I am a nutritionist and fitness instructor and I need a business card designed for my company SowGrowThrive. I provide nutrition education services such as consultations, cooking demonstrations, workshops, and supermarket tours. I also provide fitness instruction and training to clients to help overhaul their lifestyle.

I would like to see designs that have a natural, organic, feel using earthy colours. I would like to have cards printed on recycled paper.

I would prefer a 2 sided card. Front side with just the business name Sow Grow Thrive and underneath Nutrition Health Fitness. The second side to have the contact details.

The final design should communicate health and wellness through eating organic wholefoods and being physically active.

Although I have this idea, I would be open to see other suggestions that have a similar look and feel.
Updates

Target Market(s)

people interested in being healthier, women wanting to loose weight, mothers wanting to be healthier for their families

Industry/Entity Type

Nutrition

Contact Information for Business Card

Nadia Crewe
Nutritionist and Personal Trainer
M 0417582936
E sowgrowthrivenutrition@mailbox-example.net

Logo Text

SowGrowThrive (underneath) Nutrition Health Fitness

Logo styles of interest
Wordmark Logo
Requirements
Nice to have
• I like the idea of having the letters of SowGrowThrive spelt out with food such as grains, nuts, seeds, legumes, fruit etc. For example close up images of cherry tomatoes, chia seeds, kidney beans, chickpeas, blue berries, raspberries, brown rice - lots of different colours and textures. Continuing playing on the idea of the book cover Dig Rest Glow.

food is important - I am not selling supplements rather I am promoting the enjoyment of healthy wholefoods so food is important to the look and feel of the design
Should not have
• cartoon images
images associated with body building or supplements
fruit or dumb bells with tape measures around them
clichés for weight loss such as scales and tape measures
I don't want to look like other typical wellness services such as massage or spa services

```html
<!DOCTYPE html>
<html lang="en">
<head>
<meta charset="utf-8">
<title>SowGrowThrive – Business Card</title>
<link rel="stylesheet" href="https://fonts.googleapis.com/css2?family=Source+Sans+3:wght@400;600&display=swap">
<style>
  :root {
    --page: #efe9df;
    --card: #ffffff;
    --leaf: #4a9a12;
    --sun: #fbb80f;
    --ink-soft: #5b5b5b;
    --shadow: rgba(60, 45, 25, 0.18);
  }
  * { box-sizing: border-box; margin: 0; padding: 0; }
  html, body {
    width: 950px; height: 1200px; overflow: hidden;
    background: var(--page);
    font-family: "Source Sans 3", "Myriad Pro", Arial, sans-serif;
  }
  .canvas { position: relative; width: 950px; height: 1200px; }
  .card {
    position: absolute; left: 95px; width: 760px; height: 438px;
    background: var(--card); border-radius: 26px; overflow: hidden;
    box-shadow: 0 4px 14px var(--shadow);
  }
  .card--front { top: 62px; }
  .card--back { top: 616px; }
  .card__art { position: absolute; inset: 0; width: 100%; height: 100%; }

  .brand { position: absolute; text-align: center; }
  .brand__row { display: flex; align-items: center; justify-content: center; gap: 10px; }
  .brand__dot { width: 22px; height: 22px; border-radius: 50%; background: var(--sun); }
  .brand__name { font-size: 36px; font-weight: 600; color: var(--leaf); letter-spacing: 0.2px; }
  .brand__tagline { margin-top: 2px; font-size: 14px; color: var(--ink-soft); letter-spacing: 0.3px; }
  .card--front .brand { left: 140px; top: 150px; width: 300px; }
  .card--back .brand { left: 0; right: 0; top: 180px; }

  .person { position: absolute; right: 52px; top: 66px; text-align: right; }
  .person__name { font-size: 44px; font-weight: 400; color: var(--leaf); line-height: 1; }
  .person__role { margin-top: 8px; font-size: 14px; color: var(--sun); }

  .contact { position: absolute; right: 36px; top: 288px; list-style: none; text-align: right; }
  .contact__item {
    display: flex; align-items: center; justify-content: flex-end; gap: 12px;
    height: 31px; font-size: 18.5px; color: var(--sun);
  }
  .contact__icon { width: 20px; height: 20px; flex: none; }

  .back-email {
    position: absolute; left: 0; right: 0; top: 388px;
    text-align: center; font-size: 18.5px; color: var(--sun);
  }
</style>
</head>
<body>
<main class="canvas">

  <section class="card card--front" aria-label="Business card front">
    <svg class="card__art" viewBox="0 0 641 369" preserveAspectRatio="none" aria-hidden="true">
      <path d="M0,0 H137 C60,100 38,260 140,369 H0 Z" fill="var(--leaf)"/>
      <path d="M72,140 C62,235 175,330 305,369 H145 C66,300 55,220 72,140 Z" fill="var(--sun)"/>
    </svg>

    <div class="brand">
      <div class="brand__row">
        <span class="brand__dot"></span>
        <span class="brand__name">SowGrowThrive</span>
      </div>
      <p class="brand__tagline">Nutrition Health Fitness</p>
    </div>

    <div class="person">
      <h1 class="person__name">Nadia Crewe</h1>
      <p class="person__role">Nutritionist and Personal Trainer</p>
    </div>

    <ul class="contact">
      <li class="contact__item">0417582936 E
        <svg class="contact__icon" viewBox="0 0 20 20" aria-hidden="true">
          <rect x="6" y="2" width="8" height="16" rx="1.5" fill="var(--leaf)"/>
          <rect x="7.5" y="4" width="5" height="5" fill="#fff"/>
          <rect x="9" y="0" width="1.6" height="3" fill="var(--leaf)"/>
        </svg>
      </li>
      <li class="contact__item">sowgrowthrivenutrition@mailbox-example.net
        <svg class="contact__icon" viewBox="0 0 20 20" aria-hidden="true">
          <rect x="2" y="5" width="16" height="11" fill="var(--leaf)"/>
          <path d="M2,5 L10,11 L18,5 M2,16 L8,10 M18,16 L12,10" stroke="#fff" stroke-width="1.3" fill="none"/>
        </svg>
      </li>
      <li class="contact__item">www.sowgrowthrive-example.net
        <svg class="contact__icon" viewBox="0 0 20 20" aria-hidden="true">
          <g fill="none" stroke="var(--leaf)" stroke-width="1.5">
            <circle cx="10" cy="10" r="8"/>
            <ellipse cx="10" cy="10" rx="3.5" ry="8"/>
            <path d="M2,10 H18 M3.5,6 H16.5 M3.5,14 H16.5"/>
          </g>
        </svg>
      </li>
    </ul>
  </section>

  <section class="card card--back" aria-label="Business card back">
    <div class="brand">
      <div class="brand__row">
        <span class="brand__dot"></span>
        <span class="brand__name">SowGrowThrive</span>
      </div>
      <p class="brand__tagline">Nutrition Health Fitness</p>
    </div>
    <p class="back-email">sowgrowthrivenutrition@mailbox-example.net</p>
  </section>

</main>
</body>
</html>
```